Flyer Design Project

we need a new flyer to use as a permanent back cover to monthly promotional offers.

we are a gravity fitness centre. this means our classes and workouts are the type that allow you to use your own natural body weight.

We use Yoga, Vibration technology, Pilates combined with 30 years experience in the gym/fitness industry to steer you to a fitness plan that you can stick to.

we have a studio, a small gym and a Pilates reformer room.

we know that coming to a regular fitness class is a pain , we aim to make it quick fun and painless !

Price to suit every pocket! drop in pay as you go !

Small personal space,Local ,fun, professional with a community feel.

The colours are deep shocking pink black and white .

the final design should be uncluttered and informative.

I want to use the five leaf flower design within the leaflet , see attachment .

Should have a call to actions on it -

Any yoga class £5 with this leaflet
Free consultation with this leaflet .

more detail and some photographs waiting to be uploaded.

many thanks Marta

Target Market(s)

mostly womes aged between 30 - 55

Industry/Entity Type

Industry

Requirements
Must have
• one page A5 size, easy to read.
Nice to have
• as inroduction

```html
<!DOCTYPE html>
<html lang="en">
<head>
<meta charset="utf-8">
<title>Talla Fit Flyer</title>
<link rel="stylesheet" href="https://fonts.googleapis.com/css2?family=Montserrat:wght@600;700&family=Arimo:wght@400;700&display=swap">
<style>
  :root {
    --pink-deep: #c20a7e;
    --pink-main: #e0249a;
    --pink-glow: #ffd3ee;
    --white: #ffffff;
    --black: #141014;
    --price-red: #e3001b;
    --body-soft: #ffe3f3;
  }
  * { margin: 0; padding: 0; box-sizing: border-box; }
  html, body { width: 846px; height: 1200px; overflow: hidden; background: var(--white); }
  .flyer {
    position: relative;
    width: 846px;
    height: 1200px;
    overflow: hidden;
    font-family: "Arimo", Arial, sans-serif;
    color: var(--white);
    background:
      radial-gradient(ellipse 520px 200px at 50% 80px, rgba(255,211,238,0.55) 0%, rgba(255,211,238,0) 75%),
      linear-gradient(180deg, var(--pink-main) 0%, var(--pink-deep) 55%, var(--pink-main) 100%);
  }
  .brand-title {
    position: absolute; top: 30px; left: 0; width: 100%;
    text-align: center;
    font-family: "Montserrat", Arial, sans-serif;
    font-weight: 700; font-size: 92px; line-height: 1;
    letter-spacing: 2px;
  }
  .tagline {
    position: absolute; top: 128px; left: 0; width: 100%;
    text-align: center;
    font-family: "Montserrat", Arial, sans-serif;
    font-weight: 600; font-size: 28px; letter-spacing: 9px;
  }
  .offer-box {
    position: absolute; left: 52px; top: 228px; width: 348px; height: 102px;
    background: var(--white);
    color: var(--pink-deep);
    font-weight: 700; font-size: 30px; line-height: 1.1;
    text-align: center;
    display: flex; align-items: center; justify-content: center;
  }
  .offer-box .price { color: var(--price-red); }
  .intro-heading {
    position: absolute; left: 56px; top: 352px; width: 330px;
    font-weight: 700; font-size: 23px; line-height: 1.15;
  }
  .services {
    position: absolute; left: 56px; top: 478px; width: 340px;
    font-size: 19px; line-height: 1.1; color: var(--body-soft);
  }
  .drop-in {
    position: absolute; left: 56px; top: 610px;
    font-weight: 700; font-size: 23px;
  }
  .community {
    position: absolute; left: 56px; top: 652px; width: 380px;
    font-weight: 700; font-size: 20px; line-height: 1.2;
  }
  .further-info {
    position: absolute; left: 56px; top: 736px;
    font-size: 19px; line-height: 1.2; color: var(--body-soft);
  }
  .partner-mark {
    position: absolute; left: 56px; top: 790px; width: 240px; height: 96px;
    background: var(--white);
    display: flex; align-items: center; justify-content: center; gap: 12px;
  }
  .partner-mark .mark-square { width: 20px; height: 20px; background: var(--pink-deep); }
  .partner-mark .mark-name { color: var(--pink-deep); font-weight: 700; font-size: 22px; }
  .hero-photo {
    position: absolute; left: 420px; top: 226px; width: 400px; height: 716px;
    background: linear-gradient(180deg, #ffffff 0%, #fbe6f2 60%, #e7a9cf 100%);
  }
  .philosophy-band {
    position: absolute; left: 230px; top: 938px; width: 540px; height: 38px;
    background: var(--black);
    text-align: center;
    font-weight: 400; font-size: 27px; line-height: 38px; letter-spacing: 1px;
    color: var(--pink-glow);
  }
  .philosophy-text {
    position: absolute; left: 60px; top: 990px; width: 726px;
    text-align: center; font-size: 15.5px; line-height: 1.3;
  }
  .philosophy-question {
    position: absolute; left: 60px; top: 1084px; width: 726px;
    text-align: center; font-size: 14.5px;
  }
  .footer-address {
    position: absolute; left: 0; top: 1126px; width: 100%;
    text-align: center; font-size: 14.5px;
  }
  .footer-contact {
    position: absolute; left: 0; top: 1148px; width: 100%;
    text-align: center; font-size: 31px;
  }
</style>
</head>
<body>
<main class="flyer">
  <h1 class="brand-title">TALLA FIT</h1>
  <p class="tagline">MOVE WITH EASE</p>

  <div class="offer-box"><p>ANY YOGA<br>CLASS FOR <span class="price">£5</span> WITH<br>THIS LEAFLET.</p></div>

  <p class="intro-heading">We Know That Coming To A Regular Fitness Class Is A Pain , We Aim To Make It Quick Fun And Painless !</p>

  <p class="services">Choose From Yoga, Vibrating Yoga Mats, Pilates , War Machine, Pregnancy Classes,Personal Training Quick Fix Plans , Specialist Classes, Price To Suit Every Pocket!</p>

  <p class="drop-in">Drop In Pay As You Go !</p>
  <p class="community">Local , Fun , Professional With A Community Feel.</p>

  <p class="further-info">Further Information &amp; Timetable<br>www.tallafit.com</p>

  <div class="partner-mark">
    <span class="mark-square"></span>
    <span class="mark-name">Tidewell</span>
  </div>

  <div class="hero-photo" role="img" aria-label="Smiling mature couple in casual wear standing together, with dumbbells in the foreground"></div>

  <h2 class="philosophy-band">SEASONAL LIVING PHILOSOPHY</h2>
  <p class="philosophy-text">Tidewell, Runs Through Everything We Do At Talla Fit. Our Unique System Of Observing Nature, Energy And The Seasons Can Encourage Good Health And May Help Prevent Illness. We Work With Your Energy To Keep You On Top Form All Year Round.</p>
  <p class="philosophy-question">Is It For You? Yes, If You Are Seeking An Easy To Follow Sustainable Way To Live A Healthier, Longer Life.</p>

  <p class="footer-address">Brook House, 12 Alder Street, Leith, Edinburgh EH6 4QX</p>
  <p class="footer-contact">T:0131 496 0190 • www.tallafit.com</p>
</main>
</body>
</html>
```